Torvel Business Cards

Business card design. dont mind if new logo is suggested.
it would be for a security company.
our clients would be bigger security companies around Australia.
have a logo done but can be replaced. see attaached. like the colors.
Need company name, person name, designation, phone and email on front.
At back company logo and name. website saddress and 2 x license numbers
would like to have 2 different background color for both sidde

Industry/Entity Type

Security

Contact Information for Business Card

round corners, front should be light in color. need logo at back with webaddress and 2 x license numners

Font styles to use
Sans Serif

Colors
f37122
faa54b
f8ba93
0255a3
0592cd
85cae6
b3d448
9bcb3c
ffffff

Requirements
Must have
• see description
Nice to have
• see description
Should not have
• should not be difficult to read or hardd to find information on card.. lets say easy on eyes yet catchy

```html
<!DOCTYPE html>
<html lang="en">
<head>
<meta charset="utf-8">
<title>Torvel Security Group – Business Cards</title>
<link rel="stylesheet" href="https://fonts.googleapis.com/css2?family=Roboto:wght@400;500;700&display=swap">
<style>
  :root {
    --backdrop: #e8e6e2;
    --card-light: #ffffff;
    --card-dark: #1e2f5e;
    --navy: #1e2d5e;
    --text-grey: #4f5157;
    --rule-grey: #8a8c90;
    --accent-blue: #1ba3c9;
    --white: #ffffff;
  }
  * { margin: 0; padding: 0; box-sizing: border-box; }
  html, body {
    width: 1200px; height: 1200px; overflow: hidden;
    background: var(--backdrop);
    font-family: "Roboto", Arial, sans-serif;
  }
  .canvas { position: relative; width: 1200px; height: 1200px; }

  .card {
    position: absolute; left: 214px; width: 773px; height: 441px;
    box-shadow: 0 6px 18px rgba(0,0,0,0.18);
  }
  .card--front { top: 150px; background: var(--card-light); }
  .card--back { top: 633px; background: var(--card-dark); }

  /* Front: brand block */
  .brand-front {
    position: absolute; left: 60px; top: 166px; width: 320px;
    display: flex; flex-direction: column; align-items: center;
  }
  .brand-front__mark {
    width: 80px; height: 80px; border-radius: 50%;
    background: var(--accent-blue);
  }
  .brand-front__name {
    margin-top: 12px; font-size: 20px; font-weight: 500;
    color: var(--navy); letter-spacing: 0.3px; white-space: nowrap;
  }

  .divider {
    position: absolute; left: 388px; top: 83px; width: 2px; height: 276px;
    background: var(--rule-grey);
  }

  /* Front: contact block */
  .contact { position: absolute; left: 422px; top: 70px; color: var(--text-grey); }
  .contact__name { font-size: 31px; font-weight: 700; color: var(--navy); line-height: 1.1; }
  .contact__title { font-size: 20px; margin-top: 4px; }
  .contact__address { margin-top: 40px; font-size: 19px; line-height: 28px; }
  .contact__list { list-style: none; margin-top: 24px; font-size: 19px; line-height: 27px; }
  .contact__list li { display: flex; align-items: center; gap: 6px; }
  .contact__icon { width: 18px; height: 18px; flex: none; }
  .contact__licence { margin-top: 20px; margin-left: 3px; font-size: 17px; }

  /* Back */
  .brand-back {
    position: absolute; left: 0; top: 100px; width: 100%;
    display: flex; flex-direction: column; align-items: center;
  }
  .brand-back__mark {
    width: 180px; height: 180px; border-radius: 50%;
    background: var(--accent-blue);
  }
  .brand-back__name {
    margin-top: 28px; font-size: 40px; font-weight: 500;
    color: var(--white); letter-spacing: 0.8px;
  }
  .back-web {
    position: absolute; left: 0; top: 383px; width: 100%;
    text-align: center; font-size: 19px; color: var(--white);
  }
</style>
</head>
<body>
<main class="canvas">

  <section class="card card--front" aria-label="Front of business card">
    <div class="brand-front">
      <div class="brand-front__mark"></div>
      <div class="brand-front__name">TORVEL SECURITY GROUP</div>
    </div>

    <div class="divider"></div>

    <div class="contact">
      <div class="contact__name">Daniel Brooks</div>
      <div class="contact__title">President &amp; CEO</div>
      <div class="contact__address">820 Harlow Street<br>Suite 410, VIC 3051</div>
      <ul class="contact__list">
        <li>
          <svg class="contact__icon" viewBox="0 0 24 24" fill="none" stroke="currentColor" stroke-width="1.8" stroke-linejoin="round">
            <path d="M5 3h4l2 5-2.5 1.5a11 11 0 0 0 6 6L16 13l5 2v4a2 2 0 0 1-2 2A16 16 0 0 1 3 5a2 2 0 0 1 2-2z"/>
          </svg>
          000-111-2222
        </li>
        <li>
          <svg class="contact__icon" viewBox="0 0 24 24" fill="none" stroke="currentColor" stroke-width="1.8">
            <rect x="3" y="5" width="18" height="14"/><path d="M3 5l9 8 9-8"/>
          </svg>
          brooks@torvel-example.com
        </li>
        <li>
          <svg class="contact__icon" viewBox="0 0 24 24" fill="none" stroke="currentColor" stroke-width="1.6">
            <circle cx="12" cy="12" r="9"/><ellipse cx="12" cy="12" rx="4" ry="9"/><path d="M3 12h18M5 7h14M5 17h14"/>
          </svg>
          www.torvel-example.com
        </li>
      </ul>
      <div class="contact__licence">2 x license numbers</div>
    </div>
  </section>

  <section class="card card--back" aria-label="Back of business card">
    <div class="brand-back">
      <div class="brand-back__mark"></div>
      <div class="brand-back__name">TORVEL SECURITY GROUP</div>
    </div>
    <div class="back-web">www.torvel-example.com</div>
  </section>

</main>
</body>
</html>
```